RTV Photography Business Card Design

I would like a business card designed in the shape of a camera.
Would like to see various camera designs. Would like to see what the card looks like in different colors. Would like to see which logo looks better on the various camera designs so please show me some with the white logo and some with the black logo. If you need a different file formats please let me know.
Project Deadline Extended Reason: My grandfather passed away and dealing with funeral plans so need to extend deadline. Added Tuesday, March 1, 2016
Project Deadline Extended
Reason: I just got back from out of town. My grandfather's passing was the primary focus for me these past few weeks and the funeral is over so now I will concentrate on picking my business card design. I really appreciate each designer who has taken the time to submit a design. Your effort has not gone unnoticed. I look forward to seeing more amazing designs.
Industry/Entity Type
Business
Contact Information for Business Card
Wren
757-418-2096
https://www.facebook.com/rtvphotographyfreelance/
DoraWren@rtv-photography.example
Look and feel

```html
<!DOCTYPE html>
<html lang="en">
<head>
<meta charset="utf-8">
<title>RTV Photography – Camera Business Cards</title>
<link rel="stylesheet" href="https://fonts.googleapis.com/css2?family=Cinzel:wght@400&family=Open+Sans:wght@400;700&display=swap">
<style>
  :root {
    --page: #ffffff;
    --panel: #bdbec0;
    --card: #000000;
    --gold: #d1953a;
    --gold-soft: #c99a45;
    --white: #ffffff;
    --seal: #1a1108;
  }
  html, body {
    margin: 0;
    padding: 0;
    width: 1200px;
    height: 715px;
    overflow: hidden;
    background: var(--page);
  }
  .presentation {
    display: block;
    width: 1200px;
    height: 715px;
  }
  .presentation-panel { fill: var(--panel); }
  .camera-body, .camera-button { fill: var(--card); }
  .brand-seal { fill: url(#sealGlow); }
  .brand-dot { fill: var(--gold-soft); }
  .brand-name {
    font-family: "Cinzel", serif;
    font-size: 15.5px;
    fill: var(--gold-soft);
  }
  .divider { stroke: var(--gold-soft); stroke-width: 1.2; }
  .divider--light { stroke: #d8d8d8; }
  .holder-name {
    font-family: "Open Sans", sans-serif;
    font-weight: 700;
    font-size: 19px;
    letter-spacing: 1.4px;
  }
  .contact-line {
    font-family: "Open Sans", sans-serif;
    font-size: 11.5px;
    letter-spacing: 0.6px;
  }
  .tone-gold { fill: var(--gold); }
  .tone-white { fill: var(--white); }
  .icon { fill: none; stroke-width: 1.2; stroke-linejoin: round; stroke-linecap: round; }
  .icon--gold { stroke: var(--gold); }
  .icon--white { stroke: var(--white); }
</style>
</head>
<body>
<svg class="presentation" viewBox="0 0 1200 715" xmlns="http://www.w3.org/2000/svg">
  <defs>
    <radialGradient id="sealGlow" cx="0.5" cy="0.3" r="0.7">
      <stop offset="0" stop-color="#1d1208"/>
      <stop offset="1" stop-color="#0c0804"/>
    </radialGradient>
  </defs>

  <rect class="presentation-panel" x="125" y="0" width="925" height="715"/>

  <!-- Card: gold edition -->
  <g class="camera-card camera-card--gold" transform="translate(168 227)">
    <rect class="camera-button" x="54" y="-5" width="47" height="20" rx="5"/>
    <rect class="camera-button" x="286" y="-17" width="78" height="30" rx="7"/>
    <rect class="camera-body" x="0" y="0" width="406" height="280" rx="18"/>
    <circle class="brand-seal" cx="216" cy="137" r="136" role="img" aria-label="Faint background brand seal"/>
    <circle class="brand-dot" cx="111" cy="125" r="26"/>
    <text class="brand-name" x="28" y="177">RTV PHOTOGRAPHY</text>
    <line class="divider" x1="206" y1="117" x2="206" y2="191"/>
    <text class="holder-name tone-gold" x="219" y="142">JOEL MARSTEN</text>
    <path class="icon icon--gold" d="M220 155 q-1 5 4 9 l2 -2 l-2 -2 l-1 1 q-2 -2 -2 -4 l1 -1 l-2 -2 z"/>
    <text class="contact-line tone-gold" x="238" y="163">+330 2715-4093</text>
    <rect class="icon icon--gold" x="219" y="170" width="9" height="6.5" rx="0.8"/>
    <path class="icon icon--gold" d="M219 170.5 l4.5 3.5 l4.5 -3.5"/>
    <text class="contact-line tone-gold" x="238" y="177">joel@marstenmail.example</text>
  </g>

  <!-- Card: white edition -->
  <g class="camera-card camera-card--white" transform="translate(602 225)">
    <rect class="camera-button" x="53" y="-5" width="48" height="20" rx="5"/>
    <rect class="camera-button" x="286" y="-18" width="78" height="30" rx="7"/>
    <rect class="camera-body" x="0" y="0" width="405" height="281" rx="18"/>
    <circle class="brand-seal" cx="216" cy="137" r="136" role="img" aria-label="Faint background brand seal"/>
    <circle class="brand-dot" cx="111" cy="125" r="26"/>
    <text class="brand-name" x="27" y="177">RTV PHOTOGRAPHY</text>
    <line class="divider divider--light" x1="206" y1="117" x2="206" y2="191"/>
    <text class="holder-name tone-white" x="219" y="142">JOEL MARSTEN</text>
    <path class="icon icon--white" d="M220 155 q-1 5 4 9 l2 -2 l-2 -2 l-1 1 q-2 -2 -2 -4 l1 -1 l-2 -2 z"/>
    <text class="contact-line tone-white" x="238" y="163">+330 2715-4093</text>
    <rect class="icon icon--white" x="219" y="170" width="9" height="6.5" rx="0.8"/>
    <path class="icon icon--white" d="M219 170.5 l4.5 3.5 l4.5 -3.5"/>
    <text class="contact-line tone-white" x="238" y="177">joel@marstenmail.example</text>
  </g>
</svg>
</body>
</html>
```